Tiroler party ecommerce site

We have a eCommerce site that needs a redesign. What we need are 3 pages: a frontpage, a product listing page and a product page.

The look has to be:
fun, modern, fresh, bright, professional look but not corporate.

Some content keywords are :
Carnival, oktoberfesten, tirol, dirndl, leder hosen, beer, women with big breast (no porn! just fun)

Some functional hints :

The frontpage needs to give a good impression of all the products on the site.
There should also be some space for campaigns or banners on the frontpage.

The product listing page should have facets (search options) and a search field.

The product page should have a few boxes such as related products, others viewed, comments etc.. (your average product page content)

All pages should show a small cart button or box and off course a kick ass menu!

Some links :

The current site http://www.alpenfeestshop.nl/

We couldn't find any site to show as inspiration most party sites are very bad!.

```html
<!DOCTYPE html>
<html lang="en">
<head>
<meta charset="utf-8">
<title>AlpenFeest Shop – Home</title>
<link href="https://fonts.googleapis.com/css2?family=Roboto:wght@300;400;500;700&family=Roboto+Condensed:wght@400;700&display=swap" rel="stylesheet">
<style>
:root{
  --sky:#29a3dd;
  --sky-dark:#1f86c0;
  --ink:#2b2f33;
  --charcoal:#34393e;
  --steel:#3c6e88;
  --red:#e8403b;
  --red-text:#d9272e;
  --grey-line:#dcdcdc;
  --text:#333;
  --soft:#f2f2f2;
  --white:#fff;
}
*{box-sizing:border-box;margin:0;padding:0}
html,body{width:981px;height:1200px;overflow:hidden}
body{background:var(--steel);font-family:"Roboto",sans-serif;color:var(--text);position:relative}
.page{position:absolute;left:65px;top:0;width:851px;height:1200px;background:var(--white)}
.abs{position:absolute}
/* top bar */
.topbar{left:84px;top:0;width:815px;height:29px;background:var(--sky);color:#fff;font-size:9px;display:flex;justify-content:space-between;align-items:center;padding:0 18px}
.topbar nav span{margin-left:6px}
.topbar nav i{font-style:normal;margin-left:6px;opacity:.7}
/* header */
.header{left:84px;top:29px;width:815px;height:90px;background:var(--ink)}
.brand{left:18px;top:16px;display:flex;align-items:center;gap:6px}
.brand .dot{width:58px;height:58px;border-radius:50%;background:var(--sky)}
.brand b{font-family:"Roboto",sans-serif;font-weight:400;font-size:28px;color:#fff}
.cart{right:17px;top:28px;display:flex;height:34px}
.cart .label{background:#fff;font-size:9px;padding:0 12px;display:flex;align-items:center;color:#222}
.cart .label em{color:var(--red);font-style:normal;margin-left:3px}
.cart .btn{width:34px;background:var(--sky);display:flex;align-items:center;justify-content:center}
/* nav */
.mainnav{left:75px;top:119px;width:832px;height:36px;background:var(--sky);display:flex}
.mainnav a{color:#fff;text-decoration:none;font-size:12.5px;padding:0 24px;display:flex;align-items:center;border-right:1px solid var(--sky-dark)}
.mainnav a:first-child{padding:0 30px}
.search{right:24px;top:5px;display:flex;height:26px}
.search input{width:143px;border:0;height:26px}
.search .go{width:40px;background:var(--red);display:flex;align-items:center;justify-content:center}
/* promo */
.promo{left:84px;top:178px;width:815px;height:63px;background:linear-gradient(90deg,#eee,#f8f8f8 60%,#eee)}
.promo .tag{background:var(--red);color:#fff;font-size:13px;padding:2px 6px;position:absolute}
.truck{left:32px;top:12px;width:100px;height:42px}
.badge{left:418px;top:-1px;width:130px;height:65px;border-radius:50%;background:var(--red);color:#fff;text-align:center;font-weight:700;font-size:10px;line-height:1.1;display:flex;flex-direction:column;justify-content:center}
.badge strong{font-size:20px}
.phone{left:608px;top:14px;display:flex;align-items:center;gap:10px;color:var(--red);font-size:20px;font-weight:300}
/* campaigns */
.camp{left:83px;width:197px;overflow:hidden;border:1px solid #ccc}
.camp .art{width:100%;height:100%}
.camp .cap{position:absolute;left:0;bottom:0;width:100%;height:21px;background:rgba(40,40,40,.8);color:#fff;font-size:12px;text-align:center;line-height:21px}
.camp .head{position:absolute;left:0;top:0;width:100%;height:37px;background:rgba(41,163,221,.85);color:#fff;text-align:center;font-size:11px;padding-top:5px}
.camp .head small{display:block;font-size:7px}
.camp .more{position:absolute;left:65px;top:42px;background:var(--red);color:#fff;font-size:7px;padding:3px 4px;font-weight:700}
/* slider */
.slider{left:293px;top:262px;width:606px;height:252px}
.slider .art{width:100%;height:100%;background:linear-gradient(90deg,#e8e8e8,#d9d6d2 40%,#c8c3bd 70%,#b94a3e)}
.welcome{right:0;top:2px;background:var(--sky);color:#fff;font-size:14px;padding:3px 5px;font-weight:300}
.info{right:0;top:30px;width:275px;height:112px;background:rgba(80,80,80,.85);color:#fff;font-size:11.5px;padding:10px 9px;line-height:1.25}
.info .shop{position:absolute;left:97px;top:72px;background:var(--red);padding:4px 6px;font-size:12px}
.info .from{position:absolute;left:11px;top:77px;font-size:11.5px}
.slider .bar{position:absolute;left:0;bottom:0;width:100%;height:32px;background:rgba(60,60,60,.6)}
.dots{position:absolute;left:291px;top:11px;display:flex;gap:4px}
.dots i{width:9px;height:9px;background:#fff}
.dots i:first-child{background:var(--sky)}
/* categories */
.cats{left:83px;top:535px;width:197px;height:227px;border:1px solid #ccc}
.cats h3{background:var(--sky);color:#fff;font-weight:300;font-size:15px;height:35px;line-height:35px;padding-left:8px}
.cats ul{list-style:none;padding:3px 6px 0}
.cats li{font-size:12px;height:26.2px;line-height:26px;padding-left:19px;border-bottom:1px solid #ddd}
.cats li:last-child{border:0}
/* new products */
.newp{left:83px;top:781px;width:197px}
.newp h3{font-weight:400;font-size:15px;color:var(--red);border-bottom:1px solid var(--red);width:164px;padding-bottom:2px}
.newp h3 span{color:var(--sky)}
.item{display:flex;gap:6px;margin-top:12px}
.item .thumb{width:55px;height:56px;flex:none;background:linear-gradient(#f0ede6,#c9a77a)}
.item h4{font-size:8.5px;color:var(--sky);font-weight:400}
.item p{font-size:7px;line-height:1.6;margin-top:4px;color:#444}
.item b{color:var(--red-text);font-weight:400;font-size:12.5px}
/* products */
.prod{width:134px;height:201px;background:var(--soft)}
.prod .pic{height:124px;border-bottom:1px solid #f2b5b5;background:#fff}
.prod .name{text-align:center;font-size:12.5px;color:#444;margin-top:5px}
.prod .price{text-align:center;font-size:12.5px;color:var(--red-text);margin-top:3px}
.prod .add{position:absolute;left:23px;top:169px;width:87px;height:24px;background:var(--sky);color:#fff;font-size:11px;display:flex;align-items:center;gap:6px;padding-left:8px;border-radius:2px}
.add .plus{width:13px;height:13px;border-radius:50%;background:#fff;color:var(--sky);font-size:12px;line-height:13px;text-align:center;font-weight:700}
/* footer */
.footer{left:83px;top:973px;width:816px;height:198px;background:var(--charcoal);font-family:"Roboto Condensed",sans-serif;color:#fff}
.footer .band{height:44px;background:var(--steel)}
.footer .col{position:absolute;top:0}
.footer h4{font-weight:400;font-size:13px;height:44px;line-height:44px}
.footer ul{list-style:none;font-size:9.5px;line-height:19px;margin-top:6px}
.footer .about{font-size:9.5px;line-height:19px;margin-top:6px;width:162px}
.footer .about a{color:var(--sky)}
.news{position:absolute;left:0;bottom:0;width:100%;height:48px;background:var(--steel);display:flex;align-items:center}
.social{display:flex;gap:5px;margin-left:23px}
.social i{width:23px;height:23px;border-radius:50%;background:#555b61}
.social i:nth-child(2){background:var(--sky)}
.news .lbl{margin-left:80px;font-size:13px}
.news input{margin-left:14px;width:142px;height:26px;border:0}
.news .env{width:44px;height:26px;background:var(--red);display:flex;align-items:center;justify-content:center}
.cards{display:flex;gap:5px;margin-left:66px}
.cards i{width:33px;height:21px;background:#dfe4ea;border-radius:2px}
.bottom{left:83px;top:1178px;width:816px;display:flex;justify-content:space-between;font-size:8.5px}
.bottom span i{font-style:normal;margin:0 7px;color:#999}
.bottom .copy{color:var(--red-text)}
.top{left:930px;top:1133px;color:#fff;font-family:"Roboto Condensed",sans-serif;font-weight:700;font-size:11px;text-align:center}
</style>
</head>
<body>
<div class="page"></div>

<div class="abs topbar">
  <span>Welcom to Farmars AlpenFeest Shop</span>
  <nav><span>My Account</span><i>|</i><span>Wishlist</span><i>|</i><span>My Cart</span><i>|</i><span>Checkout</span><i>|</i><span>Log In</span></nav>
</div>

<header class="abs header">
  <div class="abs brand"><span class="dot"></span><b>AlpenFeest Shop</b></div>
  <div class="abs cart">
    <div class="label">SHOPPING CART: <em>$0.00</em></div>
    <div class="btn"><svg width="22" height="18" viewBox="0 0 22 18"><path d="M1 2h4l3 10h10l2-7H7" fill="none" stroke="#fff" stroke-width="2"/><circle cx="9" cy="15.5" r="1.6" fill="#fff"/><circle cx="17" cy="15.5" r="1.6" fill="#fff"/></svg></div>
  </div>
</header>

<nav class="abs mainnav">
  <a>HOME</a><a>INFORMATION</a><a>LINKS</a><a>CONTACT</a>
  <div class="abs search"><input aria-label="Search"><div class="go"><svg width="16" height="16" viewBox="0 0 16 16"><circle cx="6.5" cy="6.5" r="5" fill="none" stroke="#fff" stroke-width="2"/><path d="M10 10l5 5" stroke="#fff" stroke-width="2"/></svg></div></div>
</nav>

<section class="abs promo">
  <svg class="abs truck" viewBox="0 0 100 42"><path d="M0 8h14M4 16h12M0 24h14" stroke="#e8403b" stroke-width="3"/><rect x="20" y="4" width="46" height="26" fill="#e8403b"/><path d="M66 12h16l10 10v8H66z" fill="#e8403b"/><circle cx="34" cy="33" r="6" fill="#e8403b" stroke="#fff" stroke-width="2"/><circle cx="80" cy="33" r="6" fill="#e8403b" stroke="#fff" stroke-width="2"/><text x="24" y="15" fill="#fff" font-family="Roboto" font-weight="700" font-size="7">FREE</text><text x="24" y="24" fill="#fff" font-family="Roboto" font-weight="700" font-size="7">SHIPPING</text></svg>
  <span class="tag" style="left:163px;top:10px">NEDERLAND FREE <b>SHIPPING</b></span>
  <span class="tag" style="left:163px;top:34px">MONEY-BACK <b>GUARANTEE</b></span>
  <div class="abs badge"><strong>100%</strong>Money-Back<br>Guarantee</div>
  <div class="abs phone"><svg width="32" height="32" viewBox="0 0 32 32"><path d="M8 3l5 6-3 4c2 4 5 7 9 9l4-3 6 5-4 5C14 28 4 18 3 8z" fill="#e8403b"/></svg>012 345 67 89</div>
</section>

<div class="abs camp" style="top:262px;height:120px">
  <div class="art" role="img" aria-label="Colourful party costume fabric photo" style="background:linear-gradient(135deg,#e9dad0,#e96a8a 50%,#f2c14e)"></div>
  <div class="head">ALPENFEEST SHOP PROGRAM<small>ORDER YOU CSA EARLY TO ENSURE AVAILABILITY</small></div>
  <span class="more">READ MORE</span>
  <div class="cap">ACCEPTING APPLICATIONS!</div>
</div>
<div class="abs camp" style="top:396px;height:118px">
  <div class="art" role="img" aria-label="Colourful figures holding hands illustration" style="background:radial-gradient(circle at 50% 45%,#d84e8e,#4aa3d8 45%,#f4f4f4 75%)"></div>
  <div class="cap">OUR SALES CAMPAIGN!</div>
</div>

<section class="abs slider">
  <div class="art" role="img" aria-label="Woman carrying shopping bags beside leather handbags"></div>
  <div class="abs welcome">WELCOME TO ALPENFEEST SHOP WEBSITE</div>
  <div class="abs info">AlpenFeestShop.nl | Bergweg 12 | 7500 AB ENSCHEDE | 012 345 67 89 | info@alpenfeestshop.nl
    <span class="from">FROM $9.99</span><span class="shop">SHOP NOW!</span></div>
  <div class="bar"><div class="dots"><i></i><i></i><i></i></div></div>
</section>

<aside class="abs cats">
  <h3>BROWES CATEGORIES</h3>
  <ul><li>Tiroler kleding</li><li>Kleding accessoires</li><li>Tiroler schorten</li><li>Tiroler hoeden</li><li>Decoraties</li><li>Decoraties</li><li>Cadeau artikelen</li></ul>
</aside>

<aside class="abs newp">
  <h3><span>NEW</span> PRODUCTS</h3>
  <div class="item"><div class="thumb" role="img" aria-label="Bavarian apron costume photo"></div><div><h4>Sexy Schort Bayerische Mann</h4><p>Nunc facilisis sagittis ullamcorper.<br>Proin lectus ipsum, gravida et ..</p><b>€13,90</b></div></div>
  <div class="item"><div class="thumb" role="img" aria-label="Bavarian apron costume photo"></div><div><h4>Sexy Schort Bayerische Mann</h4><p>Nunc facilisis sagittis ullamcorper.<br>Proin lectus ipsum, gravida et ..</p><b>€13,90</b></div></div>
</aside>

<div class="abs prod" style="left:294px;top:535px"><div class="pic" role="img" aria-label="Red and black dirndl dress" style="background:linear-gradient(#fff 20%,#7a1e26 60%,#2a2a2a)"></div><div class="name">Product Name</div><div class="price">€85,90</div><div class="add"><span class="plus">+</span>Add to cart</div></div>
<div class="abs prod" style="left:450px;top:535px"><div class="pic" role="img" aria-label="Man in traditional vest" style="background:linear-gradient(#fff 15%,#2b3350 55%,#e9e6e0)"></div><div class="name">Product Name</div><div class="price">€79,90</div><div class="add"><span class="plus">+</span>Add to cart</div></div>
<div class="abs prod" style="left:607px;top:535px"><div class="pic" role="img" aria-label="Black hat with red band" style="background:linear-gradient(#fff,#333 35%,#e8c9b5 65%,#fff)"></div><div class="name">Product Name</div><div class="price">€24,95</div><div class="add"><span class="plus">+</span>Add to cart</div></div>
<div class="abs prod" style="left:764px;top:535px"><div class="pic" role="img" aria-label="Child in lederhosen and green hat" style="background:linear-gradient(#fff 10%,#c8473e 45%,#6b4a2e 75%,#fff)"></div><div class="name">Product Name</div><div class="price">30.88 $</div><div class="add"><span class="plus">+</span>Add to cart</div></div>

<div class="abs prod" style="left:294px;top:750px"><div class="pic" role="img" aria-label="Jerry can of snow spray" style="background:linear-gradient(#fff,#e9efc9 40%,#cfdca8)"></div><div class="name">Product Name</div><div class="price">€109,00</div><div class="add"><span class="plus">+</span>Add to cart</div></div>
<div class="abs prod" style="left:450px;top:750px"><div class="pic" role="img" aria-label="Box of purple party sweets" style="background:linear-gradient(#8ed0e4,#7a55b5 55%,#f0c944)"></div><div class="name">Product Name</div><div class="price">€1,90</div><div class="add"><span class="plus">+</span>Add to cart</div></div>
<div class="abs prod" style="left:607px;top:750px"><div class="pic" role="img" aria-label="Cartoon moose warning sign" style="background:linear-gradient(#fff,#b08a6a 50%,#fff)"></div><div class="name">Product Name</div><div class="price">€1,50</div><div class="add"><span class="plus">+</span>Add to cart</div></div>
<div class="abs prod" style="left:764px;top:750px"><div class="pic" role="img" aria-label="Yellow beer mug hat" style="background:linear-gradient(#fff,#f6e94c 40%,#f1d800)"></div><div class="name">Product Name</div><div class="price">€6,90</div><div class="add"><span class="plus">+</span>Add to cart</div></div>

<footer class="abs footer">
  <div class="band"></div>
  <div class="col" style="left:24px"><h4>ABOUT US</h4><ul><li>About Us</li><li>Customer Service</li><li>Privacy Policy</li></ul></div>
  <div class="col" style="left:231px"><h4>CUSTOMER SERVICES</h4><ul><li>Shipping &amp; Returns</li><li>Secure Shopping</li><li>Contact us</li></ul></div>
  <div class="col" style="left:438px"><h4>TERMS &amp; CONDITIONS</h4><ul><li>Press Room</li><li>Help</li><li>Terms &amp; Conditions</li></ul></div>
  <div class="col" style="left:639px"><h4>ABOUT US</h4><p class="about">Lorem ipsum dolor sit amet, consectetur adipiscing elit. Vivamus sit amet ligula lectus, a mollis diam. Nulla porttitor pulvinar elit .. <a>Read more</a></p></div>
  <div class="news">
    <div class="social"><i></i><i></i><i></i><i></i></div>
    <span class="lbl">SIGN UP FOR OUR NEWSLETTER</span>
    <input aria-label="Email address">
    <div class="env"><svg width="20" height="14" viewBox="0 0 20 14"><rect x="1" y="1" width="18" height="12" fill="none" stroke="#fff" stroke-width="1.5"/><path d="M1 1l9 7 9-7" fill="none" stroke="#fff" stroke-width="1.5"/></svg></div>
    <div class="cards"><i></i><i></i><i></i><i></i></div>
  </div>
</footer>

<div class="abs bottom">
  <span>Site Map<i>|</i>Search<i>|</i>Terms Advanced<i>|</i>Orders and Returns<i>|</i>Contact Us</span>
  <span class="copy">© 2014 AlpenFeestShop.nl is onderdeel van Feestgroep BV.</span>
</div>

<div class="abs top"><svg width="30" height="14" viewBox="0 0 30 14"><path d="M2 13L15 2l13 11" fill="none" stroke="#fff" stroke-width="2"/></svg><br>TOP</div>
</body>
</html>
```